VarnLink Signal Systems Website Design

We are an Australian based telecommunications company who specialise in the design, build and implementation of mission critical communications infrastructure. We have offices throughout Australia, New Zealand and Europe. Our Customers are operators in multiple markets from Oil & Gas, Mining, Government, Utilities, Carrier & Transportation.

We also work with large multi-national companies, that provide telecommunication and services such as; Pelvaro, Dransvik, Quorba, Talmoss and many more. We want to be able to achieve the same level of impressions and professionalism as what these companies present on their websites.

To reflect our recent move into the European market, we need our new site to reflect who we are as a company, and exhibit the fact we are not just based in Australia, but we are a global organisation. We want to have a fresh clean look, thats modern, dynamic and simple. Flat textures and colours are perfect for us to adapt to. A site that is based around content management, with a responsive design that can be used on all devices.

We have started to develop a basic design language that we would like to incorporate in our overall website design. We have attached some documents that highlight our design language and we can provide colour codes and fonts to ensure consistency.

Our existing site is: www.varnlinkss.example. Please feel free to view and pick apart items. From this example, we would massive improvement in how the site looks, feels and functions. We also want social media to form a big part of our site, with the likes of posts from chirpnet and blogs posting capabilities.

If you require anymore information about VarnLink or our requirements, please do not hesitate to contact.

Thanks and good luck!

Target Market(s)

Potential & Existing Customers, New international customers & markets, New Market Sectors, Partners, Service Providers

Industry/Entity Type

Telecommunications

Coding

Coded - Design and coding required

Number of Pages Required

5+ page

Font styles to use
Sans Serif

Requirements
Must have
• Content Management, Responsive Design for multiple device compatibility, Social media integration, use of lots of imagery, drop down menus, search capabilities
Should not have
• No flash.

```html
<!DOCTYPE html>
<html lang="en">
<head>
<meta charset="utf-8">
<title>VarnLink Signal Systems</title>
<link href="https://fonts.googleapis.com/css2?family=Open+Sans:wght@400;600;700;800&display=swap" rel="stylesheet">
<style>
:root{
  --navy:#0c2a44;
  --navy-deep:#081e33;
  --blue:#1d6fa3;
  --teal:#2b9bc8;
  --tile:#1b4e74;
  --tile-dark:#143c5c;
  --ink:#2d3a45;
  --muted:#6b7883;
  --line:#d5dde3;
  --paper:#ffffff;
  --page:#eef2f5;
}
*{box-sizing:border-box;margin:0;padding:0}
html,body{width:814px;height:1200px;overflow:hidden}
body{font-family:"Open Sans",Arial,sans-serif;background:var(--page);color:var(--ink);font-size:9px;position:relative}
.wrap{width:580px;margin:0 auto;position:relative}

.topbar{height:20px;background:var(--navy);color:#cfe0ec;font-size:8px}
.topbar .wrap{display:flex;justify-content:space-between;align-items:center;height:20px}
.topbar .mail{display:flex;align-items:center;gap:4px}

.hero{position:relative;height:300px;background:linear-gradient(160deg,#c7d3dc 0%,#8fa4b4 40%,#56708a 70%,#2f4a63 100%)}
.hero .photo{position:absolute;inset:0}
.header{position:absolute;top:0;left:117px;width:580px;background:var(--paper);box-shadow:0 2px 6px rgba(0,0,0,.2)}
.brand{height:62px;display:flex;align-items:center;padding-left:14px;gap:7px}
.brand .dot{width:14px;height:14px;border-radius:50%;background:var(--blue)}
.brand .name{font-size:17px;font-weight:700;color:var(--blue)}
.nav{display:flex;align-items:center;height:22px;border-top:1px solid var(--line);padding-left:10px}
.nav a{font-size:8px;font-weight:700;color:var(--blue);text-decoration:none;padding:0 8px;line-height:22px}
.nav a.active{background:var(--blue);color:#fff}
.nav .search{margin-left:auto;margin-right:8px;width:90px;height:14px;border:1px solid var(--line)}
.hero .caption{position:absolute;left:241px;top:225px;width:330px;text-align:center;color:#fff}
.hero h1{font-size:27px;font-weight:800;letter-spacing:.5px}
.hero p{font-size:7px;line-height:1.4;margin-top:3px;color:#e8eff4}
.btn{display:inline-block;background:var(--navy);color:#fff;font-size:7px;padding:3px 8px;margin-top:5px}
.arrow{position:absolute;top:232px;width:20px;height:28px;background:rgba(255,255,255,.75);display:flex;align-items:center;justify-content:center}
.arrow.l{left:0}.arrow.r{right:0}

.tiles{background:var(--teal);height:62px}
.tiles .wrap{display:flex;height:62px}
.tile{flex:1;background:var(--tile);border-right:2px solid var(--teal);display:flex;flex-direction:column;align-items:center;justify-content:center;gap:5px;color:#fff;font-size:6.5px;font-weight:700}
.tile:nth-child(odd){background:var(--tile-dark)}
.tile .ic{width:26px;height:26px;border-radius:50%;border:2px solid #9cc9e2;display:flex;align-items:center;justify-content:center}

.features{display:flex;gap:12px;margin-top:14px}
.feature{flex:1;height:72px;position:relative;color:#fff}
.feature .img{position:absolute;inset:0}
.feature span{position:absolute;left:8px;bottom:10px;font-size:10px;font-weight:700}
.f1 .img{background:linear-gradient(135deg,#8b9aa5,#4c5d6b)}
.f2 .img{background:linear-gradient(135deg,#3a3f47,#8a6a4a)}
.f3 .img{background:linear-gradient(135deg,#7b8894,#b58f5c)}

.lead{position:relative;height:212px;margin-top:14px;background:linear-gradient(180deg,#9fc3e0 0%,#c7dbe8 45%,#5d7387 75%,#34495c 100%)}
.lead .text{position:absolute;left:117px;top:12px;width:250px;color:#fff}
.lead h2{font-size:29px;font-weight:800;line-height:1}
.lead p{font-size:7.5px;line-height:1.45;margin-top:8px}

.cols{display:flex;gap:14px;margin-top:14px}
.col{flex:1;background:var(--paper);height:120px}
.col h3{background:var(--blue);color:#fff;font-size:8px;font-weight:700;padding:4px 8px}
.clients{display:grid;grid-template-columns:1fr 1fr 1fr;gap:10px 6px;padding:16px 8px;align-items:center;text-align:center}
.clients b{font-size:7.5px;font-weight:700;color:var(--navy)}
.form{padding:8px 10px}
.form .row{display:flex;align-items:center;height:15px;font-size:7px;font-weight:600}
.form .row label{width:42px}
.form .row i{flex:1;height:10px;border:1px solid var(--line)}
.form .send{display:block;width:30px;margin:6px auto 0;border:1px solid var(--line);font-size:6.5px;text-align:center;padding:2px 0}
.news{display:flex;gap:6px;padding:8px}
.news .thumb{width:30px;height:30px;border-radius:50%;background:linear-gradient(135deg,#a4b5c2,#5b7084);flex:none}
.news b{display:block;font-size:7px;color:var(--blue)}
.news p{font-size:6.5px;line-height:1.4;color:var(--muted);margin-top:3px}

.footer{position:absolute;left:0;right:0;top:862px;height:292px;background:var(--navy);color:#c7d6e2}
.footer .wrap{display:flex;gap:18px;padding-top:24px}
.footer .fc{flex:1}
.footer h4{font-size:9px;color:#fff;font-weight:700;margin-bottom:8px}
.footer p{font-size:6.5px;line-height:1.55}
.footer .item{margin-bottom:7px}
.footer ul{list-style:none}
.footer li{font-size:6.5px;line-height:1.5;margin-bottom:6px;padding-left:8px;position:relative}
.footer li:before{content:"";position:absolute;left:0;top:4px;width:3px;height:3px;background:var(--teal)}
.bottom{position:absolute;left:0;right:0;top:1154px;height:46px;background:var(--navy-deep);color:#8aa0b2;font-size:6.5px}
.bottom .wrap{display:flex;justify-content:space-between;padding-top:10px}
</style>
</head>
<body>

<div class="topbar"><div class="wrap">
  <span>Blog | About Us</span>
  <span class="mail"><svg width="9" height="7" viewBox="0 0 9 7"><rect x=".5" y=".5" width="8" height="6" fill="none" stroke="#cfe0ec"/><path d="M.5 .5 4.5 4 8.5 .5" fill="none" stroke="#cfe0ec"/></svg>info@varnlinkss.example</span>
</div></div>

<section class="hero">
  <div class="photo" role="img" aria-label="Engineers in hard hats reviewing plans at a communications site"></div>
  <header class="header">
    <div class="brand"><span class="dot"></span><span class="name">VarnLink</span></div>
    <nav class="nav">
      <a class="active">HOME</a><a>PRODUCTS &amp; SERVICES</a><a>SECTORS</a><a>SUPPORT</a><a>CORPORATE</a><a>CONTACT</a>
      <span class="search"></span>
    </nav>
  </header>
  <div class="caption">
    <h1>THE NEW STANDARD</h1>
    <p>We strive to achieve and meet the network solutions to exceed our clients and customer expectations. Their trust sets the standard for reliable and flexible communications across every sector.</p>
    <span class="btn">Learn More</span>
  </div>
  <span class="arrow l"><svg width="7" height="10"><path d="M6 1 1 5l5 4" fill="none" stroke="#333" stroke-width="1.5"/></svg></span>
  <span class="arrow r"><svg width="7" height="10"><path d="M1 1l5 4-5 4" fill="none" stroke="#333" stroke-width="1.5"/></svg></span>
</section>

<section class="tiles"><div class="wrap">
  <div class="tile"><span class="ic"><svg width="12" height="12"><rect x="2" y="2" width="8" height="8" fill="none" stroke="#fff"/></svg></span>TECHNOLOGY</div>
  <div class="tile"><span class="ic"><svg width="12" height="12"><path d="M1 11V5l3 2V5l3 2V2h4v9z" fill="#fff"/></svg></span>INDUSTRIES</div>
  <div class="tile"><span class="ic"><svg width="12" height="12"><circle cx="6" cy="6" r="4" fill="none" stroke="#fff" stroke-width="2"/></svg></span>SERVICES</div>
  <div class="tile"><span class="ic"><svg width="12" height="12"><path d="M1 4l5-3 5 3-5 3z M3 6v3h6V6" fill="#fff"/></svg></span>LEARNING</div>
  <div class="tile"><span class="ic"><svg width="12" height="12"><path d="M2 7a4 4 0 0 1 8 0" fill="none" stroke="#fff" stroke-width="1.5"/><rect x="1" y="7" width="2" height="3" fill="#fff"/><rect x="9" y="7" width="2" height="3" fill="#fff"/></svg></span>TECH SUPPORT</div>
  <div class="tile"><span class="ic"><svg width="12" height="12"><rect x="2" y="5" width="8" height="6" fill="#fff"/><path d="M4 5V3a2 2 0 0 1 4 0v2" fill="none" stroke="#fff" stroke-width="1.5"/></svg></span>SECURITY</div>
  <div class="tile"><span class="ic"><svg width="12" height="12"><circle cx="6" cy="6" r="5" fill="none" stroke="#fff"/><path d="M6 3v3h2" fill="none" stroke="#fff"/></svg></span>TIME &amp; TIDE</div>
</div></section>

<div class="wrap">
  <section class="features">
    <div class="feature f1"><div class="img" role="img" aria-label="Team meeting around a table"></div><span>Success Stories</span></div>
    <div class="feature f2"><div class="img" role="img" aria-label="Network equipment in a secure server room"></div><span>Security Matters</span></div>
    <div class="feature f3"><div class="img" role="img" aria-label="Technicians working at an industrial site"></div><span>Industry Trends</span></div>
  </section>
</div>

<section class="lead">
  <div role="img" aria-label="Modern glass office building under a blue sky" style="position:absolute;inset:0"></div>
  <div class="text">
    <h2>Leading the way™</h2>
    <p>As a leading international provider of voice and communications systems, we specialise in the delivery of mission and business critical networks, while providing the commitment, knowledge and experience our customers can rely on.</p>
    <span class="btn">Learn More</span>
  </div>
</section>

<div class="wrap">
  <section class="cols">
    <div class="col">
      <h3>Our Clients</h3>
      <div class="clients"><b>Pelvaro</b><b>Dransvik</b><b>Quorba</b><b>Talmoss</b><b>Pelvaro</b><b>Quorba</b></div>
    </div>
    <div class="col">
      <h3>Contact us</h3>
      <div class="form">
        <div class="row"><label>Name</label><i></i></div>
        <div class="row"><label>Email</label><i></i></div>
        <div class="row"><label>Country</label><i></i></div>
        <div class="row"><label>Phone</label><i></i></div>
        <span class="send">Send</span>
      </div>
    </div>
    <div class="col">
      <h3>Latest News</h3>
      <div class="news">
        <span class="thumb" role="img" aria-label="News story image"></span>
        <div><b>VarnLink on chirpnet: new office opens in Europe</b><p>Our team has expanded to serve new partners and customers across the region with the same trusted service and support.</p></div>
      </div>
    </div>
  </section>
</div>

<footer class="footer"><div class="wrap">
  <div class="fc"><h4>About us</h4><p>VarnLink Signal Systems is an Australian based telecommunications company that designs, builds and implements mission critical communications infrastructure for operators in oil and gas, mining, government, utilities and transport, with offices across Australia, New Zealand and Europe.</p></div>
  <div class="fc"><h4>Meet us</h4>
    <div class="item"><p><b>Australia Toll Free</b><br>1800 555 014</p></div>
    <div class="item"><p><b>New Zealand Toll Free</b><br>0800 555 027</p></div>
    <div class="item"><p><b>Europe Mobile Line</b><br>+44 7700 900 318</p></div>
  </div>
  <div class="fc"><h4>Sectors</h4><ul><li>Oil &amp; Gas</li><li>Mining</li><li>Government</li><li>Utilities</li><li>Transportation</li></ul></div>
  <div class="fc"><h4>Recent posts</h4><ul><li>A short guide to planning your next network upgrade</li><li>Field notes from our latest mining project rollout</li><li>Why secure radio links matter for utilities</li></ul></div>
</div></footer>

<div class="bottom"><div class="wrap"><span>© VarnLink Signal Systems | All rights reserved | Privacy Policy</span><span>Top ↑</span></div></div>

</body>
</html>
```